Business Cards & Stationery
Hollowmere Capital Group (Investment Firm)
Project: Business Cards & Stationery
Business Cards & Stationery  -
Creative Brief
Professional
Peter L. Vanstrom III
Registered Principal, OSJ
917 Larkspur Road Milbrook, WV 25418
peter.vanstrom@quillmark-example.com
www.HollowmereCapitalGroup-example.com
Also has to say (in smaller font): Securities and advisory services offered through Crestfield Ledger Corporation (CLC). Member TVORA/BQLX and a Registered Investment Advisor. Hollowmere Capital Group and CLC are separate and unrelated companies.
logo for Hollowmere Capital Group

```html
<!DOCTYPE html>
<html lang="en">
<head>
<meta charset="utf-8">
<title>Hollowmere Capital Group – Stationery</title>
<link href="https://fonts.googleapis.com/css2?family=Cinzel:wght@500&family=Open+Sans:wght@400;600&display=swap" rel="stylesheet">
<style>
  :root {
    --navy: #30497f;
    --navy-dark: #2a3f6e;
    --paper: #ffffff;
    --stage: #a7a8aa;
    --stage-line: #c4c5c7;
    --ink: #3d3f45;
    --muted: #6b6e75;
  }
  * { box-sizing: border-box; margin: 0; padding: 0; }
  html, body { width: 1200px; height: 684px; overflow: hidden; }
  body {
    position: relative;
    background: var(--stage);
    font-family: "Open Sans", Arial, sans-serif;
    color: var(--ink);
  }
  .stage-frame {
    position: absolute; inset: 9px;
    border: 2px solid var(--stage-line);
  }
  .sheet {
    position: absolute;
    background: var(--paper);
    box-shadow: 0 1px 3px rgba(0,0,0,.25);
    overflow: hidden;
  }
  .brand {
    position: absolute; left: 0; right: 0;
    display: flex; flex-direction: column; align-items: center;
    font-family: "Cinzel", "Times New Roman", serif;
    font-weight: 500; color: var(--navy);
    text-align: center;
  }
  .brand-mark {
    width: 16px; height: 16px;
    border: 2px solid currentColor;
    margin-bottom: 6px;
  }
  .brand-name { font-size: 13px; letter-spacing: .5px; line-height: 1.1; }
  .brand-sub { font-size: 7px; letter-spacing: 4px; margin-top: 2px; }

  /* Letterhead */
  .letterhead { left: 192px; top: 34px; width: 439px; height: 626px; }
  .letterhead .band { position: absolute; top: 0; left: 0; right: 0; height: 18px; background: var(--navy); }
  .letterhead .band-rule { position: absolute; top: 21px; left: 0; right: 0; height: 1px; background: var(--navy); }
  .letterhead .brand { top: 30px; }
  .letterhead .footer {
    position: absolute; bottom: 22px; left: 0; right: 0;
    text-align: center; font-size: 5px; line-height: 1.5; color: var(--muted);
  }

  /* Business cards */
  .card { width: 144px; height: 123px; left: 36px; }
  .card-front { top: 305px; background: var(--navy); color: #fff; }
  .card-front .brand { top: 14px; color: #fff; }
  .card-front .brand-name { font-size: 9px; }
  .card-front .brand-sub { font-size: 5px; letter-spacing: 2.5px; }
  .card-front .brand-mark { width: 12px; height: 12px; margin-bottom: 4px; }
  .card-front .disclaimer {
    position: absolute; left: 10px; right: 10px; top: 68px;
    font-size: 3.6px; line-height: 1.45; text-align: center; color: #dfe4ef;
  }
  .card-back { top: 436px; }
  .card-back .band { position: absolute; top: 0; left: 0; right: 0; height: 22px; background: var(--navy); }
  .card-back .person {
    position: absolute; top: 6px; left: 0; right: 0; text-align: center;
    font-size: 4.5px; color: #fff;
  }
  .card-back .person strong { font-weight: 600; }
  .card-back .brand { top: 32px; }
  .card-back .brand-name { font-size: 9px; }
  .card-back .brand-sub { font-size: 5px; letter-spacing: 2.5px; }
  .card-back .brand-mark { width: 12px; height: 12px; margin-bottom: 4px; }
  .card-back .contact {
    position: absolute; bottom: 9px; left: 0; right: 0; text-align: center;
    font-size: 3.8px; line-height: 1.5; color: var(--muted);
  }

  /* Envelope back */
  .envelope-back { left: 643px; top: 108px; width: 528px; height: 235px; }
  .envelope-back svg { position: absolute; inset: 0; }
  .envelope-back .flap-mark {
    position: absolute; left: 50%; top: 40px; width: 30px; height: 30px;
    margin-left: -15px; border: 3px solid #fff;
  }

  /* Envelope front */
  .envelope-front { left: 643px; top: 360px; width: 528px; height: 223px; }
  .envelope-front .band { position: absolute; top: 0; left: 0; right: 0; height: 20px; background: var(--navy); }
  .envelope-front .band-rule { position: absolute; top: 23px; left: 0; right: 0; height: 1px; background: var(--navy); }
  .envelope-front .brand { top: 34px; }
  .envelope-front .return-address {
    position: absolute; bottom: 24px; left: 0; right: 0;
    text-align: center; font-size: 5px; line-height: 1.5; color: var(--muted);
  }
</style>
</head>
<body>
  <div class="stage-frame"></div>

  <section class="sheet letterhead">
    <div class="band"></div>
    <div class="band-rule"></div>
    <div class="brand">
      <span class="brand-mark"></span>
      <span class="brand-name">Hollowmere Capital Group</span>
      <span class="brand-sub">Investments</span>
    </div>
    <div class="footer">
      917 Larkspur Road Milbrook, WV 25418 | Ph 304-555-0188 | F 304-555-0189<br>
      peter.vanstrom@quillmark-example.com | www.HollowmereCapitalGroup-example.com
    </div>
  </section>

  <section class="sheet card card-front">
    <div class="brand">
      <span class="brand-mark"></span>
      <span class="brand-name">Hollowmere Capital</span>
      <span class="brand-sub">Group</span>
    </div>
    <p class="disclaimer">Securities and advisory services offered through Crestfield Ledger Corporation (CLC). Member TVORA/BQLX and a Registered Investment Advisor. Hollowmere Capital Group and CLC are separate and unrelated companies.</p>
  </section>

  <section class="sheet card card-back">
    <div class="band"></div>
    <p class="person"><strong>Peter L. Vanstrom III</strong> | Registered Principal, OSJ</p>
    <div class="brand">
      <span class="brand-mark"></span>
      <span class="brand-name">Hollowmere Capital</span>
      <span class="brand-sub">Group</span>
    </div>
    <p class="contact">917 Larkspur Road Milbrook, WV 25418 | Ph 304-555-0188<br>peter.vanstrom@quillmark-example.com<br>www.HollowmereCapitalGroup-example.com</p>
  </section>

  <section class="sheet envelope-back">
    <svg viewBox="0 0 528 235" width="528" height="235" aria-hidden="true">
      <path d="M0 0 H528 V45 C470 95 340 110 264 112 C188 110 58 95 0 45 Z" fill="var(--navy)"/>
    </svg>
    <span class="flap-mark"></span>
  </section>

  <section class="sheet envelope-front">
    <div class="band"></div>
    <div class="band-rule"></div>
    <div class="brand">
      <span class="brand-mark"></span>
      <span class="brand-name">Hollowmere Capital Group</span>
      <span class="brand-sub">Investments</span>
    </div>
    <p class="return-address">917 Larkspur Road Milbrook, WV 25418 | Ph 304-555-0188<br>peter.vanstrom@quillmark-example.com | www.HollowmereCapitalGroup-example.com</p>
  </section>
</body>
</html>
```